Junk Removal company with existing WordPress website needs new mobile enhanced website

I am looking to have someone take my existing website and either update it with a new design and menu which is more mobile enhanced (70% of my traffic is from mobile devices and most people stay on the home page to find what they need) or create a new website from scratch to achieve my design goals. My name goal is the have to home page be quick and easy to find what the customer is looking for.
Our current website is: BrightCreekJunkOut.com and Google my business page https://g.page/brightcreekjunkout
I have attached an example the design idea I came up with for the home page based on what I would like it to look like as well as some logo files and pictures.

```html
<!DOCTYPE html>
<html lang="en">
<head>
<meta charset="utf-8">
<title>Bright Creek Junk Out – Junk Hauling & Cleanout Service</title>
<link href="https://fonts.googleapis.com/css2?family=Saira+Semi+Condensed:wght@600;700;800&family=Montserrat:wght@500;600;700&family=Poppins:wght@400;500;600&display=swap" rel="stylesheet">
<style>
:root{
  --orange:#ff8a00;
  --orange-deep:#f26b1d;
  --yellow:#ffc700;
  --ink:#1b1b1b;
  --text:#555;
  --muted:#8a8a8a;
  --peach:#fdeee4;
  --white:#fff;
  --dark:#111;
}
*{margin:0;padding:0;box-sizing:border-box}
html,body{width:1200px;height:5093px;overflow:hidden}
body{font-family:'Poppins',sans-serif;color:var(--text);background:var(--white);position:relative}
.abs{position:absolute}
.head{font-family:'Saira Semi Condensed',sans-serif;font-weight:800;text-transform:uppercase;color:var(--ink);letter-spacing:1px}
.btn{display:inline-block;background:var(--orange-deep);color:#fff;font-family:'Montserrat',sans-serif;font-weight:700;font-size:13px;letter-spacing:.5px;padding:9px 20px;border-radius:20px;text-transform:uppercase}
.ring{display:inline-block;width:30px;height:30px;border:2px solid var(--orange);border-radius:50%;border-right-color:transparent;vertical-align:middle;margin-right:-18px}

/* top bar & nav */
.topbar{top:0;left:0;width:1200px;height:36px;background:var(--dark);color:#fff;font-size:11px}
.topbar .hours{left:752px;top:11px}
.topbar .phone{left:988px;top:9px;font-size:14px;font-weight:500}
.dot{display:inline-block;width:20px;height:20px;border-radius:50%;background:var(--yellow);vertical-align:middle;margin-right:10px}
.nav{top:36px;left:0;width:1200px;height:69px;background:#fff}
.nav ul{position:absolute;left:432px;top:26px;list-style:none;display:flex;gap:34px;font-size:12px;color:#777}
.nav li.on{color:var(--orange-deep)}
.search{position:absolute;left:932px;top:20px;width:208px;height:28px;border-radius:14px;background:#eee;font-size:11px;padding:7px 14px;color:#555}
.search svg{position:absolute;right:10px;top:6px}
.logo-tab{top:0;left:0;width:228px;height:140px;background:var(--yellow);border-radius:0 0 110px 0;z-index:3}
.brand{display:flex;align-items:center;gap:10px;font-family:'Montserrat',sans-serif;font-weight:700;color:var(--ink);text-transform:uppercase;font-size:16px;line-height:1.1}
.brand i{display:block;width:46px;height:46px;border-radius:50%;background:var(--ink);flex:none}
.logo-tab .brand{position:absolute;left:56px;top:30px;width:170px}

/* hero */
.hero{top:105px;left:0;width:1200px;height:652px;background:linear-gradient(120deg,#4a1410,#8e1b17 40%,#5a1a14 70%,#2b1410)}
.hero h1{position:absolute;top:122px;left:0;width:1200px;text-align:center;font-family:'Saira Semi Condensed',sans-serif;font-weight:800;font-size:50px;line-height:60px;color:#fff;letter-spacing:1.5px;text-transform:uppercase}
.hero h1 em{font-style:normal;color:var(--yellow)}
.hero p{position:absolute;top:310px;left:390px;width:420px;text-align:center;color:#fff;font-size:12px;line-height:20px}
.hero .btn{position:absolute;top:388px;left:532px}
.hero .wave{position:absolute;left:0;bottom:-1px}

/* about */
.photo{border-radius:6px}
.about .ab1{left:184px;top:848px;width:236px;height:294px;background:linear-gradient(160deg,#8fa06a,#5b6b45 60%,#8b7a64)}
.about .ab2{left:448px;top:848px;width:158px;height:188px;background:linear-gradient(160deg,#c9d3de,#a9683f 55%,#6d8f4a)}
.about .ab3{left:368px;top:1052px;width:158px;height:188px;background:linear-gradient(160deg,#7c8a6f,#4a4f4a 50%,#b8b3a8)}
.about h2{left:692px;top:858px;font-size:34px}
.about p{left:688px;top:908px;width:340px;font-size:12px;line-height:20px}
.ticks{list-style:none;font-size:12px;color:#444}
.ticks li{height:22.5px;display:flex;align-items:center;gap:14px}
.ticks li::before{content:"";width:10px;height:10px;border:2px solid var(--orange);border-radius:50%}
.about .ticks{left:688px;top:1020px}
.badge{width:164px;height:50px;border:2px solid var(--yellow);border-radius:6px;background:#fff;display:flex;align-items:center;gap:10px;padding:0 10px}
.badge i{width:30px;height:30px;border-radius:50%;background:#e5e5e5;flex:none}
.badge b{display:block;width:80px;height:8px;border-radius:4px;background:#eee}

/* callout band */
.callout{top:1320px;left:0;width:1200px;height:337px;background:var(--orange)}
.callout h3{position:absolute;left:68px;top:92px;width:600px;font-size:23px;line-height:30px;color:#fff}
.callout .tel{position:absolute;left:62px;top:226px;color:#fff;font-size:20px;font-weight:500}
.truck{left:700px;top:1328px;width:500px;height:370px;background:linear-gradient(90deg,#d9dde3,#ffffff 40%,#e6e9ee);border-radius:14px 0 0 14px}

/* estimate */
.estimate{top:1657px;left:0;width:1200px;height:494px;background:var(--peach);border-radius:0 0 0 0}
.estimate h2{position:absolute;top:80px;left:0;width:1200px;text-align:center;font-size:30px;line-height:46px}
.step{position:absolute;top:196px;width:240px;text-align:center}
.step .ic{width:100px;height:100px;border-radius:50%;margin:0 auto;background:#fff;border-bottom:5px solid var(--orange-deep);display:flex;align-items:center;justify-content:center}
.step .ic.fill{background:var(--orange-deep);border:6px solid #fff;box-shadow:0 0 0 2px var(--orange-deep)}
.step h4{font-family:'Montserrat',sans-serif;font-size:13px;font-weight:600;color:#222;margin-top:22px}
.step p{font-size:11px;line-height:20px;color:#777;margin-top:6px}

/* services */
.sec-title{font-size:32px}
.hex{position:absolute}
.svc{position:absolute;width:330px}
.svc .num{position:absolute;left:-46px;top:-4px;font-family:'Saira Semi Condensed',sans-serif;font-size:34px;color:#f2e2d8;font-weight:700}
.svc h3{font-family:'Montserrat',sans-serif;font-weight:600;font-size:24px;color:#222;line-height:32px;position:relative}
.svc p{font-size:11.5px;line-height:20px;color:#777;margin:10px 0 12px}
.svc .checks{list-style:none;font-size:12px;color:#444}
.svc .checks li{height:30px;display:flex;align-items:center;gap:12px}
.svc .checks li::before{content:"✓";width:14px;height:14px;border:1.5px solid var(--orange-deep);border-radius:50%;font-size:9px;color:var(--orange-deep);display:flex;align-items:center;justify-content:center}
.svc .btn{margin-top:12px}

/* pricing */
.price{top:3618px;left:0;width:1200px;height:470px;background:var(--orange)}
.price h2{position:absolute;top:132px;left:0;width:1200px;text-align:center;color:#fff;font-size:32px}
.card{position:absolute;top:213px;width:211px;height:196px;background:#fff;text-align:center;padding-top:52px}
.card .n{position:absolute;top:-20px;left:86px;width:38px;height:42px;background:var(--orange-deep);color:#fff;font-weight:600;font-size:18px;line-height:42px;clip-path:polygon(50% 0,100% 25%,100% 75%,50% 100%,0 75%,0 25%)}
.card h4{font-family:'Montserrat',sans-serif;font-weight:700;font-size:13px;color:#222;margin-top:10px}
.card p{font-size:11px;line-height:20px;color:#888;padding:6px 16px 0}

/* bigger truck */
.bigger h2{top:4155px;left:0;width:1200px;text-align:center;font-size:32px}
.load{position:absolute;top:4420px;width:240px;text-align:center;font-family:'Montserrat',sans-serif;font-weight:600;font-size:13px;color:#222;line-height:30px}

/* footer */
.footer{top:4577px;left:0;width:1200px;height:484px;background:linear-gradient(180deg,#e2731a,#d86010 60%,#c45510)}
.footer .brand{position:absolute;left:59px;top:126px;color:#fff}
.footer .brand i{background:#fff}
.footer .about-f{position:absolute;left:59px;top:210px;width:236px;font-size:11.5px;line-height:20px;color:#fff}
.fcol{position:absolute;top:126px;color:#fff;font-size:11px}
.fcol h5{font-family:'Montserrat',sans-serif;font-size:18px;font-weight:600;margin-bottom:12px}
.fcol ul{list-style:none}
.fcol li{line-height:27px}
.fcol li::before{content:"- "}
.map{position:absolute;left:890px;top:158px;width:251px;height:118px;background:linear-gradient(135deg,#eef1f4,#d6dde4);border:1px solid #fff}
.cities{position:absolute;left:890px;top:286px;display:grid;grid-template-columns:150px 110px;font-size:11px;color:#fff}
.cities span{line-height:30px;display:flex;align-items:center;gap:12px}
.cities span::before{content:"";width:10px;height:10px;border:1.5px solid #fff;border-radius:50%}
.copy{top:5061px;left:0;width:1200px;height:32px;background:var(--orange-deep);color:#fff;font-size:11px;text-align:center;line-height:32px}
</style>
</head>
<body>

<!-- header -->
<div class="abs topbar">
  <div class="abs hours"><span class="dot"></span>Mon to Sat – 8AM to 6PM</div>
  <div class="abs phone"><span class="dot"></span>(555) 014-0822</div>
</div>
<div class="abs nav">
  <ul>
    <li class="on">Home</li><li>Our Services</li><li>What We Take</li><li>Service Areas</li><li>Contact Us</li>
  </ul>
  <div class="search">Search Here....
    <svg width="16" height="16" viewBox="0 0 16 16"><circle cx="7" cy="7" r="5" fill="none" stroke="#f26b1d" stroke-width="2"/><line x1="11" y1="11" x2="15" y2="15" stroke="#f26b1d" stroke-width="2"/></svg>
  </div>
</div>
<div class="abs logo-tab"><div class="brand"><i></i><span>Bright Creek Junk Out</span></div></div>

<!-- hero -->
<section class="abs hero" role="img" aria-label="Two crew members in red shirts loading a mattress into a junk removal truck">
  <h1>The Best Rated Junk<br>Hauling <em>and Cleanout</em><br><em>Service</em></h1>
  <p>Bright Creek Junk Out is a family owned &amp; operated local business offering junk removal, property cleanouts, light demolition and dumpster rental services.</p>
  <span class="btn">Learn More</span>
  <svg class="wave" width="1200" height="110" viewBox="0 0 1200 110" preserveAspectRatio="none"><path d="M0 70 C80 20 150 30 230 60 C330 100 380 30 470 40 C560 50 600 100 700 80 C780 60 790 0 880 10 C960 20 980 80 1060 70 C1130 60 1170 50 1200 60 L1200 110 L0 110 Z" fill="#fff"/></svg>
</section>

<!-- about -->
<section class="about">
  <div class="abs photo ab1" role="img" aria-label="Crew removing an old wooden deck in a backyard"></div>
  <div class="abs photo ab2" role="img" aria-label="Wooden play structure with a green slide before removal"></div>
  <div class="abs photo ab3" role="img" aria-label="Hot tub being hauled away on a dolly"></div>
  <h2 class="abs head"><span class="ring"></span> About Us</h2>
  <p class="abs">Bright Creek Junk Out is a family owned &amp; operated local business offering junk removal, property cleanouts, light demolition and dumpster rental services. Local, Professional, Affordable and Dependable.</p>
  <ul class="abs ticks">
    <li>Junk Removal</li><li>Property Cleanout</li><li>Light Demolition</li><li>Dumpster Rental</li><li>Property Cleanouts</li>
  </ul>
  <div class="abs badge" style="left:684px;top:1160px"><i></i><b></b></div>
  <div class="abs badge" style="left:858px;top:1160px"><i></i><b></b></div>
</section>

<!-- callout -->
<section class="abs callout">
  <h3 class="head"><span class="ring"></span> Our Professional &amp; Friendly Junk Removal Experts You Call. We Haul! We'll Solve All Your Junk Removal &amp; Property Cleanout Problems.</h3>
  <div class="tel"><span class="ring" style="margin-right:12px;border-right-color:var(--yellow)"></span>(555) 014-0822</div>
</section>
<div class="abs truck" role="img" aria-label="White box truck with a blue cab for junk hauling"></div>

<!-- estimate -->
<section class="abs estimate">
  <h2 class="head"><span class="ring"></span> 3 Simple Ways To Get Your<br>Estimate Today !</h2>
  <div class="step" style="left:173px">
    <div class="ic"><svg width="44" height="44" viewBox="0 0 24 24"><path d="M6.6 10.8c1.4 2.8 3.8 5.1 6.6 6.6l2.2-2.2c.3-.3.7-.4 1-.2 1.1.4 2.3.6 3.6.6.6 0 1 .4 1 1V20c0 .6-.4 1-1 1C10.6 21 3 13.4 3 4c0-.6.4-1 1-1h3.5c.6 0 1 .4 1 1 0 1.3.2 2.5.6 3.6.1.3 0 .7-.2 1z" fill="#f26b1d"/></svg></div>
    <h4>Click To CALL</h4>
    <p>CALL US today and talk to one of our friendly,local staff members.</p>
  </div>
  <svg class="abs" style="left:418px;top:232px" width="60" height="16" viewBox="0 0 60 16"><path d="M2 10 C20 4 40 12 56 6" fill="none" stroke="#f26b1d" stroke-width="1.5"/><path d="M50 2 L57 6 L51 11" fill="none" stroke="#f26b1d" stroke-width="1.5"/></svg>
  <div class="step" style="left:479px">
    <div class="ic fill"><svg width="40" height="46" viewBox="0 0 20 24"><rect x="2" y="2" width="16" height="20" rx="1" fill="none" stroke="#fff" stroke-width="1.6"/><line x1="5" y1="7" x2="15" y2="7" stroke="#fff" stroke-width="1.4"/><line x1="5" y1="11" x2="15" y2="11" stroke="#fff" stroke-width="1.4"/><line x1="5" y1="15" x2="12" y2="15" stroke="#fff" stroke-width="1.4"/></svg></div>
    <h4>Click To TEXT</h4>
    <p>TEXT US today with photos of the stuff you would like removed.</p>
  </div>
  <svg class="abs" style="left:708px;top:226px" width="76" height="26" viewBox="0 0 76 26"><path d="M2 14 C14 2 24 24 30 12 C34 4 44 20 70 8" fill="none" stroke="#f26b1d" stroke-width="1.5"/><path d="M64 3 L71 8 L65 13" fill="none" stroke="#f26b1d" stroke-width="1.5"/></svg>
  <div class="step" style="left:797px">
    <div class="ic"><svg width="48" height="40" viewBox="0 0 24 20"><rect x="2" y="3" width="20" height="14" rx="1" fill="none" stroke="#f26b1d" stroke-width="2"/><path d="M2 4 L12 11 L22 4" fill="none" stroke="#f26b1d" stroke-width="2"/></svg></div>
    <h4>Click To EMAIL</h4>
    <p>EMAIL US today what you would like us to haul away.</p>
  </div>
</section>

<!-- services -->
<section class="services">
  <h2 class="abs head sec-title" style="left:496px;top:2193px"><span class="ring"></span> Our Services</h2>

  <svg class="hex" style="left:59px;top:2274px" width="336" height="382" viewBox="0 0 336 382" role="img" aria-label="Pile of household junk, furniture and boxes in a yard">
    <defs><linearGradient id="g1" x1="0" y1="0" x2="1" y2="1"><stop offset="0" stop-color="#a8b46a"/><stop offset=".5" stop-color="#7a5a3c"/><stop offset="1" stop-color="#4c4740"/></linearGradient></defs>
    <polygon points="168,4 332,98 332,284 168,378 4,284 4,98" fill="none" stroke="#111" stroke-width="3"/>
    <polygon points="168,18 318,104 318,278 168,364 18,278 18,104" fill="url(#g1)"/>
  </svg>
  <div class="svc" style="left:684px;top:2278px">
    <span class="num">01</span><h3>Junk Removal</h3>
    <p>Don't let that junk stress you out! Bright Creek Junk Out is the one to call for all your Junk Removal needs. Our professional, affordable service can haul away virtually anything from a single item, to an entire house full. That's why our motto is...</p>
    <ul class="checks"><li>Misc.Household Junk</li><li>Furniture Removal</li><li>Mattress Removal</li><li>Hot Tub Removal</li><li>Yard Debris Removal</li></ul>
    <span class="btn">Learn More</span>
  </div>

  <div class="svc" style="left:266px;top:2722px">
    <span class="num">02</span><h3>Light Demolition &amp; Tear Down</h3>
    <p>Do you have an old shed, fence, deck, gazebo or other small structure you need removed? We offer light demolition services to get those unwanted structures off your property. You Call, We Haul!</p>
    <ul class="checks"><li>Shed Removal</li><li>Fence Removal</li><li>Deck Removal</li><li>Hot Tub Removal</li><li>Play Structure Removal</li></ul>
    <span class="btn">Learn More</span>
  </div>
  <svg class="hex" style="left:802px;top:2712px" width="340" height="384" viewBox="0 0 336 382" role="img" aria-label="Yellow excavator demolishing a building amid dust">
    <defs><linearGradient id="g2" x1="0" y1="0" x2="1" y2="1"><stop offset="0" stop-color="#8aa4b8"/><stop offset=".45" stop-color="#c8a640"/><stop offset="1" stop-color="#5a5650"/></linearGradient></defs>
    <polygon points="168,4 332,98 332,284 168,378 4,284 4,98" fill="none" stroke="#111" stroke-width="3"/>
    <polygon points="168,18 318,104 318,278 168,364 18,278 18,104" fill="url(#g2)"/>
  </svg>

  <svg class="hex" style="left:59px;top:3169px" width="336" height="384" viewBox="0 0 336 382" role="img" aria-label="Bags and boxes from a property cleanout piled on a lawn">
    <defs><linearGradient id="g3" x1="0" y1="0" x2="1" y2="1"><stop offset="0" stop-color="#9a8a7a"/><stop offset=".5" stop-color="#4f6b3a"/><stop offset="1" stop-color="#3a3834"/></linearGradient></defs>
    <polygon points="168,4 332,98 332,284 168,378 4,284 4,98" fill="none" stroke="#111" stroke-width="3"/>
    <polygon points="168,18 318,104 318,278 168,364 18,278 18,104" fill="url(#g3)"/>
  </svg>
  <div class="svc" style="left:684px;top:3172px">
    <span class="num">03</span><h3>Property Cleanouts</h3>
    <p>Bright Creek Junk Out provides full-service cleanout services. Our team of professionals will remove and haul away all unwanted items so you don't have to. Whether you have a single room, garage, storage unit or entire home that needs cleaning out, we're here and ready to help.</p>
    <ul class="checks"><li>Estate Cleanout</li><li>Residential Cleanout</li><li>Garage Cleanout</li><li>Storage Unit Cleanout</li><li>Attic Clean Out</li></ul>
    <span class="btn">Learn More</span>
  </div>
</section>

<!-- how we price -->
<section class="abs price">
  <svg class="abs" style="left:0;top:-1px" width="1200" height="80" viewBox="0 0 1200 80" preserveAspectRatio="none"><path d="M0 0 L1200 0 L1200 20 Q600 140 0 20 Z" fill="#fff"/></svg>
  <h2 class="head"><span class="ring" style="border-color:#fff;border-right-color:transparent"></span> How We Price</h2>
  <div class="card" style="left:158px"><span class="n">1</span>
    <svg width="40" height="40" viewBox="0 0 24 24"><rect x="4" y="3" width="14" height="18" rx="1" fill="none" stroke="#f26b1d" stroke-width="1.5"/><circle cx="17" cy="17" r="4" fill="#fff" stroke="#f26b1d" stroke-width="1.5"/><line x1="7" y1="8" x2="14" y2="8" stroke="#f26b1d" stroke-width="1.5"/></svg>
    <h4>Volume Based Pricing</h4><p>Our pricing is based on the amount of space your items take up in our truck.</p></div>
  <div class="card" style="left:382px"><span class="n">2</span>
    <svg width="40" height="40" viewBox="0 0 24 24"><rect x="3" y="5" width="18" height="15" rx="1" fill="none" stroke="#f26b1d" stroke-width="1.5"/><line x1="3" y1="9" x2="21" y2="9" stroke="#f26b1d" stroke-width="1.5"/><circle cx="18" cy="5" r="3" fill="#fff" stroke="#f26b1d" stroke-width="1.5"/></svg>
    <h4>Minimun Loads</h4><p>Our pricing is starts at a minimum pickup fee and goes up though twelve</p></div>
  <div class="card" style="left:607px"><span class="n">3</span>
    <svg width="40" height="40" viewBox="0 0 24 24"><rect x="5" y="2" width="14" height="20" rx="1" fill="none" stroke="#f26b1d" stroke-width="1.5"/><rect x="8" y="5" width="8" height="4" fill="none" stroke="#f26b1d" stroke-width="1.2"/><path d="M8 13h2M12 13h2M8 17h2M12 17h2" stroke="#f26b1d" stroke-width="1.5"/></svg>
    <h4>Free Estimates</h4><p>We can provide a free estimate over the phone,text or email so you know a price .</p></div>
  <div class="card" style="left:832px"><span class="n">4</span>
    <svg width="40" height="40" viewBox="0 0 24 24"><circle cx="12" cy="12" r="9" fill="none" stroke="#f26b1d" stroke-width="1.5"/><path d="M12 6v12M9 9h5a2 2 0 010 4h-4a2 2 0 000 4h5" fill="none" stroke="#f26b1d" stroke-width="1.5"/></svg>
    <h4>Upfront Pricing</h4><p>We always provide our valued customers with a firm price on-site before we .</p></div>
</section>

<!-- bigger truck -->
<section class="bigger">
  <h2 class="abs head sec-title"><span class="ring"></span> Bigger Truck,Butter Pricing !</h2>
  <svg class="abs" style="left:146px;top:4215px" width="256" height="196" viewBox="0 0 256 196" role="img" aria-label="Large dark junk truck with a pile of loaded items">
    <polygon points="160,2 244,48 244,144 160,192 76,144 76,48" fill="#a56a3a" stroke="#111" stroke-width="2"/>
    <rect x="0" y="120" width="110" height="46" rx="6" fill="#2a2a2a"/>
  </svg>
  <svg class="abs" style="left:434px;top:4215px" width="256" height="196" viewBox="0 0 256 196" role="img" aria-label="Competitor red truck with loaded items">
    <polygon points="160,2 244,48 244,144 160,192 76,144 76,48" fill="#c98a4a" stroke="#111" stroke-width="2"/>
    <rect x="0" y="110" width="120" height="50" rx="6" fill="#c42a22"/>
  </svg>
  <svg class="abs" style="left:764px;top:4215px" width="256" height="196" viewBox="0 0 256 196" role="img" aria-label="Competitor smaller blue truck with boxes">
    <polygon points="160,2 244,48 244,144 160,192 76,144 76,48" fill="#6b6f80" stroke="#111" stroke-width="2"/>
    <rect x="0" y="104" width="120" height="50" rx="6" fill="#2c4fa8"/>
  </svg>
  <div class="load" style="left:158px">7 pickup loads<br>560 cubic feet<br>21 cubic yards</div>
  <div class="load" style="left:479px">6 pickup loads<br>480 cubic feet<br>18 cubic yards</div>
  <div class="load" style="left:818px">5 pickup loads<br>400 cubic yards<br>15 cubic yards</div>
</section>

<!-- footer -->
<footer class="abs footer" role="img" aria-label="Warm orange-tinted photo of a junk truck behind footer content">
  <svg class="abs" style="left:0;top:-1px" width="1200" height="80" viewBox="0 0 1200 80" preserveAspectRatio="none"><path d="M0 0 L1200 0 L1200 10 Q600 130 0 10 Z" fill="#fff"/></svg>
  <div class="brand"><i></i><span>Bright Creek<br>Junk Out</span></div>
  <p class="about-f">Bright Creek Junk Out is a family owned &amp; operated local business offering junk removal, property cleanouts, light demolition and dumpster rental services.</p>
  <div class="fcol" style="left:338px"><h5>Site Map</h5><ul><li>Home</li><li>About Us</li><li>What We Take</li><li>Service</li><li>Services Area</li><li>Reviews</li><li>Contact Us</li></ul></div>
  <div class="fcol" style="left:613px"><h5>Services</h5><ul><li>Junk Removal &amp; Hauling</li><li>Property Cleanout</li><li>Light Demolition</li><li>Dumpster Rental</li></ul></div>
  <div class="fcol" style="left:890px"><h5>Service Area</h5></div>
  <div class="map" role="img" aria-label="Map of the service area"></div>
  <div class="cities"><span>Boise</span><span>Caldwell</span><span>Meridian</span><span>Middleton</span><span>Eagle</span><span>Garden city</span><span>Star</span><span>Kuna</span><span>Nampa</span><span>Emmett</span></div>
</footer>
<div class="abs copy">© 2021 Bright Creek Junk Out. All Rights Reserved.</div>

</body>
</html>
```